Baked goods front of bag sticker

Pebblecrest Brownies,
2 Go size (clear plastic bag of handful of ¼” square bites)
There will also be larger sizes and custom options(corporate/events) using the same image.
Deliverables Needed:
Need sticker with “Pebblecrest Brownies” for front of bag, approximate 2” circle or rectangle/square.
Packaging front sticker design should be sizable for other media, ie website, future packaging, logo.
Flavor should be indicated on second sticker that integrates well.
Back sticker is already complete and includes ingredients, company name, health dept permit, and other legal necessities. Font will be changed to integrate with front.
Flavors:
1. Sunset Maple Brownie
2. Honeycomb Glow Brownie
3. Zip Zop Mint
4. Crumbly Oat Delight (not so gooey but great)
Primary Audiences:
Anyone who wants a sweet treat to enjoy, and maybe share, on the go. Audience wants a fresh treat with real ingredients they know and love (real butter, Pure vanilla, Fresh eggs)
Audience wants something from a baker not a machine.
Sold at checkout in stores that don’t have baked goods, higher end convenience stores, specialty stores, small gourmet stores, theaters, toy stores, sports arenas, etc.
Will be sampled at events (festivals, movie screenings, races)
Tone and Image:
Fresh, Fun and frank with real ingredients you know
Because it is little and is home-baked, it should be perceived as a little treat without the guilt.
Messages:
Fresh, natural, little treat on the run.
Dear Designers,

```html
<!DOCTYPE html>
<html lang="en">
<head>
<meta charset="utf-8">
<title>Pebblecrest Brownies – Front Stickers</title>
<link rel="stylesheet" href="https://fonts.googleapis.com/css2?family=Chelsea+Market&family=Sriracha&display=swap">
<style>
  :root {
    --page: #ffffff;
    --white: #ffffff;
    --teal: #7cc6bf;
    --cocoa: #867670;
    --peach: #f5d29c;
    --rose: #e87f8e;
    --tag-orange: #f28a0c;
    --tag-green: #9bc43f;
    --tag-salmon: #efac7b;
    --tag-mauve: #b46c82;
  }
  * { box-sizing: border-box; margin: 0; padding: 0; }
  html, body {
    width: 1200px; height: 900px; overflow: hidden;
    background: var(--page);
  }
  .sheet { position: relative; width: 1200px; height: 900px; }

  .sticker {
    position: absolute;
    width: 356px; height: 356px;
    border-radius: 50%;
    background: var(--sticker-colour);
  }
  .sticker::before {
    content: "";
    position: absolute; inset: 13px;
    border: 4px solid var(--white);
    border-radius: 50%;
  }
  .sticker--maple    { left: 156px; top: 72px;  --sticker-colour: var(--teal);  --tag-colour: var(--tag-orange); }
  .sticker--mint     { left: 696px; top: 72px;  --sticker-colour: var(--cocoa); --tag-colour: var(--tag-green); }
  .sticker--honey    { left: 156px; top: 478px; --sticker-colour: var(--peach); --tag-colour: var(--tag-salmon); }
  .sticker--oat      { left: 696px; top: 478px; --sticker-colour: var(--rose);  --tag-colour: var(--tag-mauve); }

  .sticker__art {
    position: absolute;
    left: 118px; top: 40px;
    width: 108px; height: 80px;
  }

  .sticker__name {
    position: absolute;
    left: 0; right: 0; top: 124px;
    text-align: center;
    font-family: "Chelsea Market", "Georgia", serif;
    font-size: 39px;
    line-height: 56px;
    color: var(--white);
  }

  .sticker__flavour {
    position: absolute;
    left: 72px; top: 248px;
    width: 218px; height: 44px;
    background: var(--tag-colour);
    transform: rotate(-1.5deg);
    display: flex; align-items: center; justify-content: center;
    font-family: "Sriracha", "Comic Sans MS", cursive;
    font-size: 20px;
    color: var(--white);
    white-space: nowrap;
  }
</style>
</head>
<body>
<main class="sheet">

  <section class="sticker sticker--maple">
    <svg class="sticker__art" viewBox="0 0 108 80" role="img" aria-label="Illustration of a milk jug, a cookie and a sprig of wheat">
      <rect x="4" y="6" width="100" height="70" rx="18" fill="#ffffff" opacity="0.35"/>
    </svg>
    <h2 class="sticker__name">Pebblecrest<br>Brownies</h2>
    <p class="sticker__flavour">Sunset Maple</p>
  </section>

  <section class="sticker sticker--mint">
    <svg class="sticker__art" viewBox="0 0 108 80" role="img" aria-label="Illustration of a milk jug, a cookie and a sprig of wheat">
      <rect x="4" y="6" width="100" height="70" rx="18" fill="#ffffff" opacity="0.35"/>
    </svg>
    <h2 class="sticker__name">Pebblecrest<br>Brownies</h2>
    <p class="sticker__flavour">Zip Zop Mint</p>
  </section>

  <section class="sticker sticker--honey">
    <svg class="sticker__art" viewBox="0 0 108 80" role="img" aria-label="Illustration of a milk jug, a cookie and a sprig of wheat">
      <rect x="4" y="6" width="100" height="70" rx="18" fill="#ffffff" opacity="0.4"/>
    </svg>
    <h2 class="sticker__name">Pebblecrest<br>Brownies</h2>
    <p class="sticker__flavour">Honeycomb Glow</p>
  </section>

  <section class="sticker sticker--oat">
    <svg class="sticker__art" viewBox="0 0 108 80" role="img" aria-label="Illustration of a milk jug, a cookie and a sprig of wheat">
      <rect x="4" y="6" width="100" height="70" rx="18" fill="#ffffff" opacity="0.35"/>
    </svg>
    <h2 class="sticker__name">Pebblecrest<br>Brownies</h2>
    <p class="sticker__flavour">Crumbly Oat Delight</p>
  </section>

</main>
</body>
</html>
```